BRIMWELL TAVERN FRIDAY MAY 3

Flyer design for bar/nightclub event. Trying to keep a general theme with their flyers (see below) but would like to add some neon or some pop to it.

TEXT:

Brimwell Bar & Lounge Presents

MOONTIDE FRIDAYS
GRAND OPENING EVENT

PURE HOUSE MUSIC W/

VERNOX
TOMAS VEREK
BENTLER & MAJOR DRIFT

21+
9PM-130AM
418 K STREET DAVIS CA

Target Market(s)

House/dance music crowd.

Industry/Entity Type

Night Club

Font styles to use
Sans Serif

Colors
9bcb3c
fbee3d
ffffff

Requirements
Must have
• Large DJ names
Nice to have
• General theme of the attached flyers. Neon colors that stick with the theme. Anything else that looks cool will be considered

```html
<!DOCTYPE html>
<html lang="en">
<head>
<meta charset="utf-8">
<title>Moontide Fridays – Grand Opening</title>
<link rel="stylesheet" href="https://fonts.googleapis.com/css2?family=Montserrat:wght@400;500;600;700;800&display=swap">
<style>
  :root {
    --bark: #3a2e24;
    --bark-deep: #2f251d;
    --neon-yellow: #fbee3d;
    --lime: #9bcb3c;
    --pale-yellow: #eef29a;
    --forest: #7d9a3a;
    --olive: #6b7a35;
    --gold: #d8a325;
    --white: #ffffff;
  }
  * { margin: 0; padding: 0; box-sizing: border-box; }
  html, body { width: 849px; height: 1200px; overflow: hidden; background: var(--bark); }
  .flyer {
    position: relative;
    width: 849px;
    height: 1200px;
    background: var(--bark);
    font-family: "Montserrat", sans-serif;
    color: var(--bark);
    overflow: hidden;
  }
  .canopy {
    position: absolute; left: 0; top: 0; width: 849px; height: 178px;
    background: linear-gradient(180deg, #dff04a 0%, #b9de40 100%);
  }
  .canopy-trees {
    position: absolute; top: 0; width: 240px; height: 175px;
    background: radial-gradient(ellipse at center, rgba(107,122,53,0.55) 0%, rgba(107,122,53,0) 70%);
  }
  .canopy-trees.left { left: 0; }
  .canopy-trees.right { right: 0; }
  .venue-badge {
    position: absolute; left: 254px; top: 36px; width: 344px; height: 104px;
    background: var(--bark-deep);
    border: 3px solid var(--gold);
    display: flex; align-items: center; justify-content: center; gap: 16px;
  }
  .venue-badge .mark {
    width: 22px; height: 22px; background: var(--gold);
  }
  .venue-badge .name {
    color: var(--white); font-weight: 700; font-size: 25px; letter-spacing: 0.5px;
  }
  .series-title {
    position: absolute; left: 40px; top: 198px;
    font-size: 51px; font-weight: 400; color: var(--pale-yellow); letter-spacing: 1px;
    line-height: 1;
  }
  .gradient-bar {
    position: absolute;
    background: linear-gradient(90deg, var(--neon-yellow) 0%, var(--lime) 100%);
  }
  .headline-bar { left: 11px; top: 266px; width: 776px; height: 66px; }
  .headline {
    position: absolute; left: 28px; top: 8px;
    font-size: 53px; line-height: 1; white-space: nowrap;
  }
  .headline strong { font-weight: 600; }
  .headline span { font-weight: 400; }
  .genre-panel {
    position: absolute; left: 11px; top: 353px; width: 828px; height: 120px;
    background: var(--lime);
  }
  .genre {
    position: absolute; left: 28px; top: 14px;
    font-size: 43px; font-weight: 400; line-height: 1;
  }
  .lineup-name {
    display: flex; align-items: center; justify-content: center;
    font-weight: 800; font-size: 56px; letter-spacing: 1.5px; line-height: 1;
  }
  .headliner { left: 256px; top: 492px; width: 335px; height: 57px; border-radius: 29px; }
  .support { left: 11px; width: 828px; height: 59px; }
  .support.one { top: 564px; }
  .support.two { top: 638px; }
  .support.three { top: 714px; }
  .landscape {
    position: absolute; left: 0; top: 798px; width: 849px; height: 402px;
    background: linear-gradient(180deg, #9bcb3c 0%, #87aa3a 55%, #6b7a35 100%);
  }
  .details-frame {
    position: absolute; left: 11px; top: 841px; width: 642px; height: 249px;
    background: var(--bark);
    padding: 9px 8px 9px 0;
    display: flex; flex-direction: column; gap: 5px;
  }
  .detail-row {
    position: relative; flex: 1;
    background: linear-gradient(90deg, var(--neon-yellow) 0%, var(--lime) 100%);
    display: flex; align-items: center; padding-left: 20px;
    font-size: 42px; font-weight: 500; line-height: 1; white-space: nowrap;
  }
</style>
</head>
<body>
<div class="flyer">
  <div class="canopy">
    <div class="canopy-trees left" role="img" aria-label="Leafy tree branches reaching in from the top left corner"></div>
    <div class="canopy-trees right" role="img" aria-label="Leafy tree branches reaching in from the top right corner"></div>
  </div>

  <div class="venue-badge">
    <div class="mark"></div>
    <div class="name">BRIMWELL BAR &amp; LOUNGE</div>
  </div>

  <h1 class="series-title">MOONTIDE FRIDAYS</h1>

  <div class="gradient-bar headline-bar">
    <p class="headline"><strong>GRAND OPENING</strong> <span>EVENT</span></p>
  </div>

  <div class="genre-panel">
    <p class="genre">HOUSE MUSIC W/</p>
  </div>

  <div class="gradient-bar headliner lineup-name">VERNOX</div>
  <div class="gradient-bar support one lineup-name">TOMAS VEREK</div>
  <div class="gradient-bar support two lineup-name">BENTLER</div>
  <div class="gradient-bar support three lineup-name">MAJOR DRIFT</div>

  <div class="landscape" role="img" aria-label="Green meadow with a silhouetted pine forest on the right"></div>

  <div class="details-frame">
    <div class="detail-row">21+</div>
    <div class="detail-row">FRIDAY MAY 3 2019</div>
    <div class="detail-row">9PM-130AM</div>
    <div class="detail-row">418 K STREET DAVIS CA</div>
  </div>
</div>
</body>
</html>
```